IT COMPANYcutting edge tec business card

we are IT company that building any apps.
we need business card in japanese and english
You don’t have to include all information in front one you can attach part of that information to back-side
company name : 株式会社ひかりの丘 (BRIGHTHILL Inc.)
concept : cutting-edge technology
role : 取締役 (director)
name : 呉 炫秀 (Oh Hyeonsuk)
post number : 154-0038
address : 東京都世田谷区西若葉台5-14-8 (5-14-8, Nishiwakabadai, Setagaya Ku, Tokyo To, 154-0038, Japan)
Tel:+81-3-5917-2846
Mobile:+81-80-7253-3169
Email : hoh@brighthill-lab.com
website : www.brighthill-lab.com

we dont have logo so please make it as well
we also looking for designer who can make homapage design.

Contact Information for Business Card

cutting-edge design and modern for IT

Font styles to use
Sans Serif

Colors
34a6d7
33b8a4
6092c4
3377b5
886aae
6b449b
b868aa
a64599

Requirements
Must have
• Simple but designed

```html
<!DOCTYPE html>
<html lang="ja">
<head>
<meta charset="utf-8">
<title>株式会社ひかりの丘 — Business Card</title>
<link href="https://fonts.googleapis.com/css2?family=Noto+Sans+JP:wght@400;500&family=Open+Sans:wght@400;500&display=swap" rel="stylesheet">
<style>
  :root {
    --bg: #2b2c2f;
    --card-white: #f4f4f6;
    --brand-blue: #3478b6;
    --brand-green: #33b8a4;
    --text-blue: #2f6fb0;
    --photo-light: #e9eef5;
    --photo-mid: #b9b6cc;
    --photo-dark: #9a97b4;
  }
  * { margin: 0; padding: 0; box-sizing: border-box; }
  html, body { width: 1200px; height: 1000px; overflow: hidden; }
  body {
    background: var(--bg);
    font-family: "Noto Sans JP", "Open Sans", sans-serif;
    position: relative;
  }
  .card {
    position: absolute;
    left: 200px;
    width: 800px;
    height: 470px;
    overflow: hidden;
    box-shadow: 0 8px 24px rgba(0,0,0,.45);
  }

  /* Card back: photo with company name */
  .card-back { top: 15px; }
  .card-back .photo {
    position: absolute; inset: 0;
    background:
      linear-gradient(180deg, rgba(255,255,255,0) 55%, rgba(190,188,210,.55) 100%),
      linear-gradient(90deg, var(--photo-light) 0%, var(--photo-mid) 30%, var(--photo-dark) 50%, var(--photo-mid) 72%, var(--photo-light) 100%);
  }
  .card-back .brand {
    position: absolute;
    left: 0; right: 0; top: 250px;
    display: flex; align-items: center; justify-content: center; gap: 18px;
    color: var(--text-blue);
    font-size: 40px; font-weight: 400; letter-spacing: 2px;
  }
  .brand-dot {
    width: 48px; height: 48px; border-radius: 50%;
    background: var(--brand-blue);
  }

  /* Card front: contact details */
  .card-front { top: 510px; background: var(--card-white); }
  .card-front .shapes { position: absolute; inset: 0; }
  .card-front .brand {
    position: absolute;
    left: 40px; top: 205px; width: 300px;
    display: flex; align-items: center; gap: 12px;
    color: var(--brand-green);
    font-size: 26px; letter-spacing: 1px;
  }
  .card-front .brand .brand-dot { width: 30px; height: 30px; background: var(--brand-green); }

  .person { position: absolute; left: 470px; top: 90px; color: var(--text-blue); }
  .person-name { font-size: 32px; font-weight: 500; letter-spacing: 2px; line-height: 1.1; }
  .person-role { font-size: 22px; margin-top: 2px; }

  .address {
    position: absolute; left: 450px; top: 200px;
    color: var(--text-blue);
    font-family: "Open Sans", "Noto Sans JP", sans-serif;
    font-size: 20px; line-height: 1.2; letter-spacing: .5px;
  }
  .address .ja { font-family: "Noto Sans JP", sans-serif; }

  .contacts {
    position: absolute; left: 435px; top: 300px;
    list-style: none;
    color: var(--text-blue);
    font-family: "Open Sans", sans-serif;
    font-size: 22px; letter-spacing: .6px;
  }
  .contacts li { display: flex; align-items: center; gap: 12px; height: 38px; }
  .contacts svg { width: 28px; height: 28px; flex: none; }
</style>
</head>
<body>

<section class="card card-back" aria-label="Card back">
  <div class="photo" role="img" aria-label="Photo of a business team in silhouette standing before large office windows"></div>
  <div class="brand"><span class="brand-dot"></span><span>株式会社ひかりの丘</span></div>
</section>

<section class="card card-front" aria-label="Card front">
  <svg class="shapes" viewBox="0 0 800 470" preserveAspectRatio="none" aria-hidden="true">
    <polygon points="280,470 400,320 425,380 345,470" fill="var(--brand-green)"/>
    <polygon points="345,470 415,395 400,470" fill="var(--brand-blue)"/>
    <polygon points="0,0 370,0 410,310 265,470 0,470" fill="var(--brand-blue)"/>
  </svg>

  <div class="brand"><span class="brand-dot"></span><span>株式会社ひかりの丘</span></div>

  <div class="person">
    <p class="person-name">呉 炫秀</p>
    <p class="person-role">取締役</p>
  </div>

  <div class="address">
    <p class="ja">東京都世田谷区西若葉台5-14-8</p>
    <p>Ku, Tokyo To, 154-0038, Japan</p>
    <p>p.o:154-0038</p>
  </div>

  <ul class="contacts">
    <li>
      <svg viewBox="0 0 28 28"><circle cx="14" cy="14" r="12.5" fill="none" stroke="var(--brand-green)" stroke-width="2"/><path d="M8 12c0-2 3-3 6-3s6 1 6 3v1h-3v-1.5h-6V13H8z M10 14h8l1 5H9z" fill="var(--brand-green)"/></svg>
      <span>+81-3-5917-2846</span>
    </li>
    <li>
      <svg viewBox="0 0 28 28"><circle cx="14" cy="14" r="12.5" fill="none" stroke="var(--brand-green)" stroke-width="2"/><path d="M10 7l3 3-1.5 2c1 2 2.5 3.5 4.5 4.5l2-1.5 3 3-2 2c-5 0-11-6-11-11z" fill="var(--brand-green)"/></svg>
      <span>+81-80-7253-3169</span>
    </li>
    <li>
      <svg viewBox="0 0 28 28"><circle cx="14" cy="14" r="14" fill="var(--brand-green)"/><rect x="7" y="9" width="14" height="10" fill="#fff"/><path d="M7 9l7 6 7-6" fill="none" stroke="var(--brand-green)" stroke-width="1.5"/></svg>
      <span>hoh@brighthill-lab.com</span>
    </li>
    <li>
      <svg viewBox="0 0 28 28"><circle cx="14" cy="14" r="12.5" fill="none" stroke="var(--brand-green)" stroke-width="2"/><g fill="none" stroke="var(--brand-green)" stroke-width="1.4"><circle cx="14" cy="14" r="8"/><ellipse cx="14" cy="14" rx="3.5" ry="8"/><path d="M6 14h16M7.5 10h13M7.5 18h13"/></g></svg>
      <span>www.brighthill-lab.com</span>
    </li>
  </ul>
</section>

</body>
</html>
```